Postcard design to acquire new clients for my Property Management Company

I'm looking for a postcard design that I can send to prospective clients detailing information about my company and services.
Postcard should be eye catching and contain information from www.brightkeyrentals-example.com. I've provided a few screen shots for the most important information and my logo.
Target Market(s)
Real Estate
Industry/Entity Type
Real Estate
Font styles to use
Sans Serif
Requirements
Must have
- Must be eye catching!! this will be a direct mail piece - I'd like for the card to be read and not tossed in the trash immediately.
Design que from the logo.
A place to write / print the receipts name and address.
our physical address - 2287 Marble Lane, Lubbock, TX 79555.
Should not have
- the contact information on the business card is not accurate - please use info from website.

```html
<!DOCTYPE html>
<html lang="en">
<head>
<meta charset="utf-8">
<title>BrightKey Rentals – Property Management Flyer</title>
<link rel="stylesheet" href="https://fonts.googleapis.com/css2?family=Montserrat:wght@300;400;500;700;900&family=Roboto+Condensed:wght@400&display=swap">
<style>
  :root{
    --brand-blue:#2a5d94;
    --deep-blue:#1f4f82;
    --ink:#1a1a1a;
    --grey:#a9a9ab;
    --light-grey:#c9ccd1;
    --bar-grey:#b9babc;
    --paper:#ffffff;
    --stage:#dfe4ea;
  }
  *{margin:0;padding:0;box-sizing:border-box}
  html,body{width:1200px;height:795px;overflow:hidden;background:var(--stage)}
  body{position:relative;font-family:"Montserrat",sans-serif}
  .flyer{position:absolute;left:337px;top:12px;width:526px;height:770px;background:var(--paper);overflow:hidden;box-shadow:0 6px 20px rgba(0,0,0,.18)}
  .abs{position:absolute}
  .brand-name{left:0;width:100%;top:26px;text-align:center;font-weight:700;font-size:30px;letter-spacing:5px;color:var(--brand-blue);white-space:nowrap}
  .hero{left:0;top:84px;width:526px;height:242px}
  .headline{left:27px;top:118px;font-weight:900;font-size:31px;line-height:29.5px;color:var(--light-grey);letter-spacing:-1px;text-transform:uppercase;white-space:nowrap}
  .tagline{left:48px;top:316px;width:440px;height:21px;background:var(--bar-grey);color:var(--brand-blue);font-size:11.5px;font-weight:400;line-height:21px;text-align:center;white-space:nowrap;box-shadow:2px 2px 3px rgba(0,0,0,.25)}
  .plan{top:353px;width:126px}
  .plan-title{background:var(--brand-blue);color:#fff;font-weight:900;font-size:11.5px;height:16px;line-height:16px;padding-left:6px;letter-spacing:-.3px;white-space:nowrap}
  .plan-price{background:var(--ink);color:#fff;height:55px;padding:3px 6px 0;white-space:nowrap}
  .plan-sub{font-size:9.5px;line-height:12px}
  .plan-rate{font-weight:900;font-size:30px;line-height:28px;letter-spacing:-1px}
  .plan-unit{font-size:9.5px;line-height:10px}
  .plan-features{list-style:none;margin-top:8px;padding-left:6px;font-family:"Roboto Condensed",sans-serif;font-size:9px;line-height:14px;color:var(--ink);white-space:nowrap;letter-spacing:-.1px}
  .divider{top:360px;width:1px;height:180px;background:var(--brand-blue)}
  .services-bar{left:74px;top:563px;width:392px;height:23px;background:#fff;box-shadow:2px 2px 3px rgba(0,0,0,.25);display:flex;white-space:nowrap}
  .services-title{width:152px;background:var(--brand-blue);color:#fff;font-size:17px;font-weight:300;line-height:23px;padding-left:8px}
  .services-note{font-size:8.4px;line-height:23px;padding-left:8px;color:var(--ink)}
  .service{width:60px;text-align:center;font-size:7.4px;line-height:7.5px;color:var(--ink)}
  .service svg{display:block;margin:0 auto 3px}
  .web-box{left:300px;top:655px;width:226px;height:23px;background:var(--ink);color:#fff;font-size:10px;line-height:23px;padding-left:9px;white-space:nowrap}
  .contact-title{left:66px;top:684px;width:429px;font-size:23px;font-weight:300;color:#fff;border-bottom:1px solid #fff;line-height:30px;white-space:nowrap}
  .contact-item{top:729px;font-size:10.5px;line-height:12.5px;color:var(--deep-blue);display:flex;gap:6px;align-items:center;white-space:nowrap}
</style>
</head>
<body>
<main class="flyer">
  <div class="abs brand-name">BRIGHTKEY RENTALS</div>

  <svg class="abs hero" viewBox="0 0 526 242" width="526" height="242">
    <defs>
      <linearGradient id="photoTone" x1="0" y1="0" x2="1" y2="1">
        <stop offset="0" stop-color="#b8a28a"/>
        <stop offset=".5" stop-color="#d9cbbb"/>
        <stop offset="1" stop-color="#8ea3b8"/>
      </linearGradient>
    </defs>
    <rect width="526" height="242" fill="url(#photoTone)" role="img" aria-label="Photo of a smiling couple receiving the keys to their new rental home"/>
    <polygon points="0,0 248,0 312,242 0,242" fill="var(--brand-blue)"/>
  </svg>

  <h1 class="abs headline">Choose<br>the right<br>property<br>management<br>system</h1>

  <div class="abs tagline">Maximize your financial returns with support from our rental specialists</div>

  <section class="abs plan" style="left:48px">
    <div class="plan-title">LEASE ONLY</div>
    <div class="plan-price"><div class="plan-sub">You Just Need Tenants</div><div class="plan-rate">9%</div><div class="plan-unit">of annual lease</div></div>
    <ul class="plan-features"><li>Professional Photography</li><li>Marketing &amp; Advertising</li><li>Property Showings</li><li>Tenant Screening &amp; Qualifications</li><li>Lease Execution</li><li>Move In Coordination</li></ul>
  </section>
  <div class="abs divider" style="left:184px"></div>
  <section class="abs plan" style="left:194px">
    <div class="plan-title">FULL SERVICE</div>
    <div class="plan-price"><div class="plan-sub">Our Most Popular</div><div class="plan-rate">10%</div><div class="plan-unit">of monthly rent</div></div>
    <ul class="plan-features"><li>Includes Leasing Service</li><li>24/7 Emergency Response</li><li>Move In &amp; Out Inspections</li><li>Professional Lease Enforcement</li><li>Schedule &amp; Oversee all Repairs</li><li>Pay all Invoices</li><li>Monthly &amp; Year End Statements</li><li>Annual Market Rent Analysis</li></ul>
  </section>
  <div class="abs divider" style="left:327px"></div>
  <section class="abs plan" style="left:337px">
    <div class="plan-title">PREMIUM SERVICE</div>
    <div class="plan-price"><div class="plan-sub">Our Premier Service</div><div class="plan-rate">12%</div><div class="plan-unit">of monthly rent</div></div>
    <ul class="plan-features"><li>Includes Full Service Features</li><li>Professional Video Marketing</li><li>Home Warranty Coordination</li><li>Tenant Retention Program</li></ul>
  </section>

  <svg class="abs" style="left:0;top:520px" width="526" height="250" viewBox="0 0 526 250">
    <polygon points="0,3 526,114 526,250 0,250" fill="var(--grey)"/>
    <line x1="150" y1="34" x2="526" y2="114" stroke="var(--brand-blue)" stroke-width="1.5"/>
  </svg>

  <div class="abs services-bar"><div class="services-title">OUR SERVICES</div><div class="services-note">We offer full-service property management solutions</div></div>

  <div class="abs service" style="left:61px;top:598px"><svg width="22" height="22" viewBox="0 0 22 22"><circle cx="11" cy="11" r="11" fill="var(--brand-blue)"/><path d="M5 11.5 11 6l6 5.5M7 10.5V16h8v-5.5" fill="none" stroke="#fff" stroke-width="1.8"/></svg>Property<br>Marketing</div>
  <div class="abs service" style="left:129px;top:598px"><svg width="22" height="22" viewBox="0 0 22 22"><circle cx="11" cy="11" r="11" fill="var(--brand-blue)"/><circle cx="8" cy="8.5" r="2.3" fill="#fff"/><circle cx="14" cy="8.5" r="2.3" fill="#fff"/><path d="M4 16a4 4 0 0 1 8 0zM10 16a4 4 0 0 1 8 0z" fill="#fff"/></svg>Tenant<br>Screening</div>
  <div class="abs service" style="left:184px;top:598px"><svg width="22" height="22" viewBox="0 0 22 22"><circle cx="11" cy="11" r="11" fill="var(--brand-blue)"/><text x="11" y="15.5" text-anchor="middle" font-family="Montserrat,sans-serif" font-weight="900" font-size="13" fill="#fff">$</text></svg>Rent<br>Collection</div>
  <div class="abs service" style="left:239px;top:598px"><svg width="22" height="22" viewBox="0 0 22 22"><circle cx="11" cy="11" r="11" fill="var(--brand-blue)"/><path d="M7 16 14 8M11.5 6.5l5 2.5-2 2" fill="none" stroke="#fff" stroke-width="2"/></svg><br>Maintenance</div>

  <div class="abs service" style="left:61px;top:646px"><svg width="22" height="22" viewBox="0 0 22 22"><circle cx="11" cy="11" r="11" fill="var(--brand-blue)"/><circle cx="9.5" cy="9.5" r="3.5" fill="none" stroke="#fff" stroke-width="1.8"/><path d="M12 12l4.5 4.5" stroke="#fff" stroke-width="2"/></svg>Property<br>Inspections</div>
  <div class="abs service" style="left:129px;top:646px"><svg width="22" height="22" viewBox="0 0 22 22"><circle cx="11" cy="11" r="11" fill="var(--brand-blue)"/><path d="M6 6v10h10" fill="none" stroke="#fff" stroke-width="1.3"/><rect x="8" y="10" width="1.6" height="5" fill="#fff"/><rect x="10.7" y="8" width="1.6" height="7" fill="#fff"/><rect x="13.4" y="11" width="1.6" height="4" fill="#fff"/></svg>Financial<br>Reporting</div>
  <div class="abs service" style="left:184px;top:646px"><svg width="22" height="22" viewBox="0 0 22 22"><circle cx="11" cy="11" r="11" fill="var(--brand-blue)"/><path d="M11 4.5 16 6.5v4c0 3-2 5-5 6.5-3-1.5-5-3.5-5-6.5v-4z" fill="#fff"/></svg>Evictions</div>
  <div class="abs service" style="left:239px;top:646px"><svg width="22" height="22" viewBox="0 0 22 22"><circle cx="11" cy="11" r="11" fill="var(--brand-blue)"/><path d="M11 5v11M7 16h8M5.5 7h11M5.5 7l-2 4h4zM16.5 7l-2 4h4z" fill="none" stroke="#fff" stroke-width="1.2"/></svg>Legal<br>Guidance</div>

  <div class="abs web-box">www.brightkeyrentals-example.com</div>

  <h2 class="abs contact-title">CONTACT OUR TEAM</h2>

  <div class="abs contact-item" style="left:44px">
    <svg width="12" height="16" viewBox="0 0 12 16"><path d="M6 0a6 6 0 0 1 6 6c0 4-6 10-6 10S0 10 0 6a6 6 0 0 1 6-6z" fill="var(--brand-blue)"/><circle cx="6" cy="6" r="2.2" fill="var(--grey)"/></svg>
    <span>2287 Marble Lane,<br>Lubbock, TX 79555.</span>
  </div>
  <div class="abs contact-item" style="left:180px">
    <svg width="14" height="14" viewBox="0 0 14 14"><circle cx="7" cy="7" r="6.2" fill="none" stroke="var(--brand-blue)" stroke-width="1.2"/><path d="M5 4c-1 1-1 5 2 6.5l1-1.3-1.3-1L6.2 6 7 5.2z" fill="var(--brand-blue)"/></svg>
    <span>Give us a call now:<br>(555) 014-2290</span>
  </div>
  <div class="abs contact-item" style="left:306px">
    <svg width="15" height="11" viewBox="0 0 15 11"><rect x=".6" y=".6" width="13.8" height="9.8" fill="none" stroke="var(--brand-blue)" stroke-width="1.2"/><path d="M.6.6 7.5 6l6.9-5.4M.6 10.4l5-4.3M14.4 10.4l-5-4.3" fill="none" stroke="var(--brand-blue)" stroke-width="1.1"/></svg>
    <span style="font-size:9.4px">Email us:<br>info@brightkeyrentals-example.com</span>
  </div>
</main>
</body>
</html>
```